Borrowed Lanterns - the new thriller in the Tidewater series by award-winning author Marta K. Belloway

Looking for an book cover design for the 4th book in the Tidewater series by Marta K. Belloway. Covers from the first 3 books are attached. Would like to keep a series look going, so possibly using a hand holding a paint brush might work - but not tied down to showing a hand on the cover. Most of the book takes place in a rustic Arizona desert estate in a national forest - so something depicting a desert scene might work too. The cover needs to convey a "thriller" feeling. Attached is our design template with needed specs. Also attached are two other covers for inspiration:

A GARDEN UNDER SALT - something like this could work in the key were a paintbrush and the scene is set in the Arizona desert

THE ORCHARD AT NOON - this could work too with Arizona desert setting

Here's the synopsis of BORROWED LANTERNS:

Her life ended and she is disappointed to discover she is still alive.

With all ties to her handler or anyone connected to her life as a hired killer, she struggles to understand who and even what she has become. She knows she doesn’t want to kill again. And yes, danger finds her and she responds, animal-like, in the only way she knows how.

In this mood of absolute bereavement, she comes across Harriet Vasquell, a world famous artist who has spent the last three decades living a hermit-like existence on a rustic desert estate in a national forest.

Harriet invites her to stay on to assist the old woman who will, in return, mentor our narrator as she deepens her own interest in art.

What is not at first apparent is that elements of Harriet’s past are shrouded in danger, sorrow and darkness and rather than growing as an artist, she soon finds herself enmeshed in a dangerous mystery with strands that stretch decades into the past.

```html
<!DOCTYPE html>
<html lang="en">
<head>
<meta charset="utf-8">
<title>Borrowed Lanterns — Marta K. Belloway</title>
<link rel="stylesheet" href="https://fonts.googleapis.com/css2?family=Anton&family=Oswald:wght@400;600&family=Roboto+Condensed:ital,wght@0,700;1,400&display=swap">
<style>
  :root {
    --night: #0b0806;
    --ember: #5a1a0c;
    --sunset: #e0611c;
    --glow: #f5a33a;
    --title-red: #c8202a;
    --white: #ffffff;
    --quote-grey: #e9e4df;
  }
  html, body {
    margin: 0;
    padding: 0;
    width: 811px;
    height: 1200px;
    overflow: hidden;
    background: var(--night);
  }
  .cover {
    position: relative;
    width: 811px;
    height: 1200px;
    overflow: hidden;
    background: var(--night);
  }
  .desert-sunset {
    position: absolute;
    left: 0;
    top: 0;
    width: 811px;
    height: 1000px;
    background:
      radial-gradient(ellipse 260px 120px at 400px 830px, var(--glow) 0%, rgba(245,163,58,0) 100%),
      linear-gradient(to bottom,
        var(--night) 0%,
        #160b08 28%,
        #3a1309 45%,
        var(--ember) 56%,
        #a8351a 66%,
        var(--sunset) 73%,
        #b8401c 78%,
        #2a0d07 84%,
        var(--night) 92%);
  }
  .endorsement {
    position: absolute;
    top: 24px;
    left: 0;
    width: 100%;
    text-align: center;
    color: var(--white);
  }
  .endorsement-quote {
    margin: 0;
    font-family: "Roboto Condensed", sans-serif;
    font-weight: 700;
    font-size: 30px;
    letter-spacing: 0.2px;
  }
  .endorsement-source {
    margin: 4px 0 0;
    font-family: "Roboto Condensed", sans-serif;
    font-size: 19px;
    color: var(--quote-grey);
  }
  .endorsement-source .name { font-weight: 700; font-style: normal; }
  .endorsement-source .role { font-style: italic; }
  .book-title {
    position: absolute;
    top: 148px;
    left: 0;
    width: 100%;
    margin: 0;
    text-align: center;
    font-family: "Anton", sans-serif;
    font-weight: 400;
    line-height: 1;
    text-transform: uppercase;
  }
  .title-first {
    display: block;
    color: var(--title-red);
    font-size: 124px;
    letter-spacing: 1px;
  }
  .title-second {
    display: block;
    color: var(--white);
    font-size: 112px;
    margin-top: 8px;
    letter-spacing: 2px;
  }
  .genre-label {
    position: absolute;
    top: 984px;
    left: 0;
    width: 100%;
    text-align: center;
    margin: 0;
    font-family: "Oswald", sans-serif;
    font-weight: 400;
    font-size: 24px;
    letter-spacing: 5px;
    color: var(--white);
  }
  .author-name {
    position: absolute;
    top: 1030px;
    left: 0;
    width: 100%;
    text-align: center;
    margin: 0;
    font-family: "Oswald", sans-serif;
    font-weight: 600;
    font-size: 56px;
    letter-spacing: 2px;
    color: var(--title-red);
    text-transform: uppercase;
  }
</style>
</head>
<body>
  <main class="cover">
    <div class="desert-sunset" role="img" aria-label="Desert sunset with saguaro cactus silhouettes against an orange sky"></div>

    <section class="endorsement">
      <p class="endorsement-quote">“Brilliant. Terrifying. Compulsively readable.”</p>
      <p class="endorsement-source"><span class="name">–ROSALIND MARSH,</span> <span class="role">Harbor Ledger Best-selling author</span></p>
    </section>

    <h1 class="book-title">
      <span class="title-first">Borrowed</span>
      <span class="title-second">Lanterns</span>
    </h1>

    <p class="genre-label">A NOVEL</p>
    <p class="author-name">Marta K. Belloway</p>
  </main>
</body>
</html>
```